Report Cover

This is for a Binder Front, Side, Back. I have uploaded a few examples. We are an education resource company that delivers data in a format that allows districts to make better decisions. Our color palette is uploaded as well.

```html
<!DOCTYPE html>
<html lang="en">
<head>
<meta charset="utf-8">
<title>Comprehensive Needs Assessment – Binder Cover</title>
<link href="https://fonts.googleapis.com/css2?family=Oswald:wght@500;600;700&family=Poppins:wght@400;500&display=swap" rel="stylesheet">
<style>
  :root{
    --stage:#5e5e5e;
    --paper:#f7f8fa;
    --mist:#e4e8ee;
    --mist-deep:#d6dde6;
    --cream:#f3efe4;
    --navy:#3d4a85;
    --gold:#c9a23c;
    --teal:#15a29b;
    --ink:#2b2b2b;
    --leaf:#8dc63f;
  }
  *{box-sizing:border-box;margin:0;padding:0}
  html,body{width:720px;height:1200px;overflow:hidden}
  body{background:var(--stage);position:relative;font-family:'Poppins',sans-serif}

  .binder{
    position:absolute;left:10px;top:347px;width:700px;height:506px;
    background:linear-gradient(135deg,var(--paper) 0%,#fff 45%,var(--mist) 100%);
    box-shadow:0 4px 14px rgba(0,0,0,.35);overflow:hidden;
  }
  .binder-texture{position:absolute;inset:0;width:100%;height:100%}
  .panel{position:absolute;top:0;height:100%}
  .panel--back{left:0;width:322px}
  .panel--spine{left:322px;width:53px}
  .panel--front{left:375px;width:325px}

  .headline{font-family:'Oswald',sans-serif;font-weight:600;line-height:1;text-align:center;text-transform:uppercase;white-space:nowrap}
  .c-navy{color:var(--navy)} .c-gold{color:var(--gold)} .c-teal{color:var(--teal)}
  .year{font-family:'Poppins',sans-serif;font-weight:500;color:var(--navy);letter-spacing:.12em;text-align:center;line-height:1}

  /* back */
  .back-title{position:absolute;left:40px;width:249px;top:24px}
  .back-title .kicker{font-size:16.5px;font-weight:500;letter-spacing:-.3px}
  .back-title .district{font-size:36px;font-weight:700;margin-top:6px}
  .back-title .district-sub{font-size:25px;font-weight:600;margin-top:1px}
  .back-title .year{font-size:20px;margin-top:4px}
  .back-summary{position:absolute;left:40px;top:146px;width:249px;font-size:6.6px;line-height:8.2px;color:var(--ink);text-align:justify;text-align-last:center}

  .brand-mark{display:flex;align-items:center;gap:4px;font-family:'Poppins',sans-serif;font-weight:500;color:var(--ink);line-height:1.1}
  .brand-mark .dot{width:14px;height:14px;border-radius:50%;background:var(--leaf);flex:none}
  .back-brand{position:absolute;left:39px;top:425px;font-size:9px;width:92px}
  .back-contact{position:absolute;right:33px;top:422px;text-align:right}
  .back-contact .company{font-family:'Oswald',sans-serif;font-weight:500;font-size:11.5px;color:var(--navy);text-transform:uppercase;white-space:nowrap;margin-bottom:2px}
  .back-contact p{font-size:7.5px;line-height:8.5px;color:var(--ink)}

  /* spine */
  .spine-text{position:absolute;left:0;right:0;top:30px;display:flex;flex-direction:column;align-items:center}
  .spine-kicker{writing-mode:vertical-rl;font-family:'Oswald',sans-serif;font-weight:600;font-size:13.5px;line-height:14px;color:var(--navy);text-transform:uppercase}
  .spine-district{writing-mode:vertical-rl;font-family:'Oswald',sans-serif;font-weight:700;font-size:16px;color:var(--gold);text-transform:uppercase;margin-top:16px;letter-spacing:.02em;white-space:nowrap}
  .spine-year{writing-mode:vertical-rl;font-family:'Poppins',sans-serif;font-weight:500;font-size:15px;color:var(--navy);letter-spacing:.15em;margin-top:12px}

  /* front */
  .front-brand{position:absolute;left:108px;top:28px;font-size:10px;width:120px}
  .front-title{position:absolute;left:0;right:0;top:84px}
  .front-title .line{font-size:27px;font-weight:600;letter-spacing:.2px}
  .front-art{position:absolute;left:18px;top:140px;width:288px;height:206px;border-radius:6px;
    background:radial-gradient(ellipse at 55% 45%,#5fc9d6 0%,#7d8cc8 35%,rgba(227,200,120,.55) 62%,rgba(247,248,250,0) 80%)}
  .front-district{position:absolute;left:0;right:0;top:364px}
  .front-district .district{font-size:45px;font-weight:700;letter-spacing:.3px}
  .front-district .district-sub{font-size:34px;font-weight:600;margin-top:1px}
  .front-district .year{font-size:35px;margin-top:4px}
</style>
</head>
<body>
<main class="binder" aria-label="Binder cover: back, spine and front">
  <svg class="binder-texture" viewBox="0 0 700 506" preserveAspectRatio="none" aria-hidden="true">
    <path d="M0 0 H140 C110 60 40 70 0 110 Z" fill="var(--mist)"/>
    <path d="M0 420 C60 390 150 430 210 470 C240 490 260 500 270 506 H0 Z" fill="var(--mist-deep)" opacity=".55"/>
    <path d="M200 250 C260 230 310 270 322 330 V506 H240 C280 440 190 360 200 250 Z" fill="var(--cream)" opacity=".6"/>
    <path d="M375 0 H470 C440 40 400 60 375 70 Z" fill="var(--mist)"/>
    <path d="M560 150 C620 130 700 170 700 230 V420 C650 380 600 300 560 150 Z" fill="var(--cream)" opacity=".7"/>
    <path d="M700 0 V90 C660 70 640 30 620 0 Z" fill="var(--mist-deep)" opacity=".6"/>
    <path d="M375 470 C420 440 500 470 560 506 H375 Z" fill="var(--mist-deep)" opacity=".5"/>
    <circle cx="470" cy="78" r="12" fill="#fff"/>
    <circle cx="120" cy="34" r="9" fill="#fff"/>
    <circle cx="250" cy="396" r="6" fill="#fff"/>
  </svg>

  <section class="panel panel--back" aria-label="Back cover">
    <header class="back-title">
      <h2 class="headline c-navy kicker">Comprehensive Needs Assessment</h2>
      <h1 class="headline c-gold district">Willowmere</h1>
      <p class="headline c-teal district-sub">School District</p>
      <p class="year">2024</p>
    </header>
    <p class="back-summary">Lorem ipsum dolor sit amet, consectetur adipiscing elit, sed do eiusmod tempor incididunt ut labore et dolore magna aliqua. Magna sit amet purus gravida quis. Mollis nunc sed id semper risus. Amet tellus cras adipiscing enim eu turpis egestas, in nulla posuere sollicitudin aliquam. Purus non enim praesent elementum facilisis leo. Tristique et egestas quis ipsum suspendisse ultrices gravida dictum fusce. At ultrices mi tempus imperdiet nulla malesuada pellentesque elit eget. Ipsum faucibus vitae aliquet nec ullamcorper sit amet risus nullam. Morbi quis commodo odio aenean sed adipiscing diam. Cras fermentum odio eu feugiat pretium nibh ipsum consequat. Id faucibus nisl tincidunt eget nullam. Elit duis tristique sollicitudin nibh sit amet commodo nulla facilisi. Ut pharetra sit amet aliquam id diam maecenas ultricies mi. Turpis in eu mi bibendum neque egestas. Nunc non blandit massa enim nec dui nunc mattis enim. Hendrerit gravida rutrum quisque non tellus orci ac auctor. Egestas pretium aenean pharetra magna ac. Luctus accumsan tortor posuere ac ut consequat semper viverra. Tempor orci eu lobortis elementum nibh tellus. Morbi enim nunc faucibus a pellentesque sit amet porttitor eget. Vitae et leo duis ut. Auctor elit sed vulputate mi sit amet mauris. Diam quam nulla porttitor massa id neque aliquam. Vestibulum morbi blandit cursus risus. Tortor pretium viverra suspendisse potenti nullam ac. Dapibus ultrices in iaculis nunc sed. Donec ultrices tincidunt arcu non sodales neque sodales. Vitae tortor condimentum lacinia quis vel eros donec ac odio. Nulla facilisi morbi tempus iaculis. Nulla aliquet porttitor lacus luctus. Consectetur lorem donec massa sapien.</p>
    <div class="brand-mark back-brand"><span class="dot" aria-hidden="true"></span><span>Learnwise Data Partners, LLC</span></div>
    <address class="back-contact" style="font-style:normal">
      <div class="company">Learnwise Data Partners, LLC</div>
      <p>4127 cedar hollow lane</p>
      <p>Fairbrook , ms 38801</p>
      <p>555.014.2290</p>
    </address>
  </section>

  <section class="panel panel--spine" aria-label="Spine">
    <div class="spine-text">
      <p class="spine-kicker">Comprehensive<br>Needs Assessment</p>
      <p class="spine-district">Willowmere School District</p>
      <p class="spine-year">2024</p>
    </div>
  </section>

  <section class="panel panel--front" aria-label="Front cover">
    <div class="brand-mark front-brand"><span class="dot" aria-hidden="true"></span><span>Learnwise Data Partners, LLC</span></div>
    <header class="front-title">
      <h2 class="headline c-navy line">Comprehensive</h2>
      <h2 class="headline c-gold line">Needs Assessment</h2>
    </header>
    <div class="front-art" role="img" aria-label="Isometric illustration of stacked books topped with rising charts, surrounded by people reviewing data, a magnifying glass and bar graphs"></div>
    <footer class="front-district">
      <h1 class="headline c-gold district">Willowmere</h1>
      <p class="headline c-teal district-sub">School District</p>
      <p class="year">2024</p>
    </footer>
  </section>
</main>
</body>
</html>
```